Flyer Design

We are a new service called chatpal.co.uk (see website) This is a premium rate £1:50 per sms text advice service. I am a qualified counsellor who already runs a practice see gavinrowecounselling.uk and have gotten per,it's ion from CALLTARIFFHUB and are registered with them for this service. Quite simply they text Q4 followed by a brief description of their personal dilemma/life or relationship concern to 64915 this is received by me and then I text back with a brief piece of guidance and feedback on their issue. So it is a text based counselling/advice service for those who want a day to day life issue dealt with in confidence,quickly and discreetly. I want the flyers to be basic with a basic and easily transferable and identifiable image like the one on my website.

Industry/Entity Type

Counsellor

```html
<!DOCTYPE html>
<html lang="en">
<head>
<meta charset="utf-8">
<title>chatpal.co.uk flyer</title>
<link rel="stylesheet" href="https://fonts.googleapis.com/css2?family=Open+Sans:wdth,wght@75..100,300..800&family=Fjalla+One&display=swap">
<style>
:root{
  --stage:#5b5e63;
  --sky-top:#dfe6ef;
  --sky-mid:#c9d3de;
  --warm:#e7c9a4;
  --grass:#6f8a48;
  --brand-blue:#3aa3f2;
  --navy:#3d5c85;
  --band-top:#f3f5f8;
  --band-mid:#9fb2cb;
  --band-low:#6f88a9;
  --paper:#dde3ec;
  --ink:#3a3f47;
  --ink-soft:#555b63;
  --rule:#aab4c2;
}
*{margin:0;padding:0;box-sizing:border-box}
html,body{width:1200px;height:1000px;overflow:hidden}
body{background:var(--stage);font-family:"Open Sans",sans-serif;color:var(--ink);position:relative}

.page{position:absolute;top:92px;height:826px;overflow:hidden}
.page--front{left:8px;width:588px}
.page--back{left:606px;width:586px;background:var(--paper)}

/* front */
.front-photo{position:absolute;inset:0;
  background:
    radial-gradient(ellipse 55% 40% at 50% 62%, #8a6a58 0%, rgba(138,106,88,0) 70%),
    linear-gradient(180deg,var(--sky-top) 0%,var(--sky-mid) 32%,#d8cbb8 52%,var(--warm) 66%,#9aa070 84%,var(--grass) 100%);}
.brand-box{position:absolute;left:48px;top:44px;width:440px;height:82px;border-radius:16px;background:var(--brand-blue)}
.brand-name{position:absolute;left:48px;top:44px;width:440px;height:82px;display:flex;align-items:center;justify-content:center;
  font-weight:600;font-size:60px;color:#fff;letter-spacing:-1px}
.front-question{position:absolute;left:0;width:100%;top:146px;text-align:center;font-weight:300;font-size:20px;color:var(--ink)}
.front-cta{position:absolute;left:0;width:100%;top:173px;text-align:center;font-family:"Fjalla One",sans-serif;font-size:21px;color:var(--ink)}
.front-cta em{font-style:normal;color:var(--brand-blue)}
.front-note{position:absolute;left:0;width:100%;top:199px;text-align:center;font-style:italic;font-size:12.5px;color:var(--ink-soft)}
.reverse-note{position:absolute;left:456px;top:226px;font-style:italic;font-size:13px;line-height:15px;color:var(--ink-soft);text-align:right;width:96px}
.reverse-arrow{position:absolute;left:424px;top:214px}
.price-badge{position:absolute;left:392px;top:436px;width:144px;height:144px;border-radius:50%;background:var(--brand-blue);
  border:4px solid #fff;box-shadow:0 0 0 3px var(--brand-blue);color:#fff;text-align:center;font-family:"Fjalla One",sans-serif}
.price-badge .amount{display:block;font-size:54px;line-height:56px;margin-top:18px}
.price-badge .unit{display:block;font-size:20px;line-height:22px}

/* back */
.back-strap{height:53px;background:var(--navy);color:#fff;font-family:"Fjalla One",sans-serif;font-size:21px;display:flex;align-items:center;justify-content:center}
.back-band{height:80px;background:linear-gradient(180deg,var(--band-top) 0%,var(--band-mid) 30%,var(--band-low) 100%);display:flex;align-items:center;justify-content:center}
.back-band .brand-name{position:static;width:auto;height:auto;font-size:62px}
.back-body{padding:28px 34px 0 31px;font-stretch:85%;font-size:10.6px;line-height:11.4px;color:var(--ink-soft)}
.back-body h2{font-size:19.5px;font-weight:700;color:var(--ink);line-height:24px;margin-bottom:5px;font-stretch:90%}
.back-body p{margin-bottom:11px}
.back-body .caps{text-transform:uppercase}
.how{margin-top:22px}
.how ul{list-style:none;text-transform:uppercase}
.how li{position:relative;padding-left:12px;margin-bottom:7px}
.how li::before{content:"•";position:absolute;left:1px;top:0}
.how strong{color:var(--ink)}
.divider{border:0;border-top:1px solid var(--rule);margin:30px 0 24px}
.small-print{font-size:7.2px;line-height:11px;text-transform:uppercase}
</style>
</head>
<body>

<section class="page page--front">
  <div class="front-photo" role="img" aria-label="Photograph of a smiling young woman with long brown hair texting on a phone, outdoors in soft evening light"></div>
  <div class="brand-box"></div>
  <div class="brand-name">chatpal.co.uk</div>
  <p class="front-question">Do you need quick and professional help with a dilemma?</p>
  <p class="front-cta">JUST TEXT <em>Q4</em> FOLLOWED BY YOUR ISSUE TO <em>64915</em></p>
  <p class="front-note">(in under 160 characters per text)</p>
  <svg class="reverse-arrow" width="40" height="80" viewBox="0 0 40 80" aria-hidden="true">
    <path d="M30 4 C6 14 2 44 26 62" fill="none" stroke="var(--brand-blue)" stroke-width="9" stroke-linecap="round"/>
    <path d="M14 56 L38 70 L16 79 Z" fill="var(--brand-blue)"/>
  </svg>
  <p class="reverse-note">See reverse for more details</p>
  <div class="price-badge"><span class="amount">£1.50</span><span class="unit">PER TEXT</span></div>
</section>

<section class="page page--back">
  <div class="back-strap">JUST TEXT Q4 FOLLOWED BY YOUR ISSUE TO 64915</div>
  <div class="back-band"><span class="brand-name">chatpal.co.uk</span></div>
  <div class="back-body">
    <h2>WHO ARE WE &amp; WHAT DO WE DO?</h2>
    <p>Firstly it's important to know: We are registered with CALLTARIFFHUB which means we have sought the appropriate guidance and permission when establishing this service.</p>
    <p>We are a short-term, one-off confidential emotional support SMS service. This is not designed to be a prolonged relationship. It is meant to be brief, informative and cost effective intervention. Essentially it is a professional counsellor just a text away. All you need to do is send a message briefly describing your query (this is typically questions and difficulties you would experience in your day to day life and relationships).</p>
    <p class="caps">I am a qualified counsellor with many years experince of dealing with a variety of clients from adolescents to adults. In part of my day to day life I run a small but effective private counselling practice. My clients range from adolescents to adults,men and women. I am trained as an integrative counsellor which means im knowledgeable in various models of counselling and can adapt our communicatin to meet your needs.</p>
    <p class="caps">I always aim to offer each indiviual warmth,genuinesss and respect no matter the duration of their contact or presentig problem or concern.</p>

    <div class="how">
      <h2>HOW IT WORKS:</h2>
      <ul>
        <li>We are &nbsp;a premium rate text support and guidance service operated by fully qualified practicing counsellors.</li>
        <li>It is simple &amp; straight forwrd.simply start your message with either mate or Q4 followed by a brief description of your issue and send it to 64915. You will then receive a personalised response from a qualified and highly &nbsp;experienced counsellor.</li>
        <li>You need not wrestle with life on your own nor do you need to rely on the biased advice of loved ones. There is no need to stay worried and anxious unclear and unsure. No more will you face the confusion of online search engine advice,get support quickly and privately from the comfort and privacy of your own surroundings.</li>
        <li>From difficulties in work to problems in relationships or worries in yourself we are here to help</li>
        <li>Counselling is a valuable and life changing experience but one that is not possible for everyone so we offer the same listening and non judgemental approach direct to your phone this of course can be read and kept or delted if you need to.</li>
        <li><strong>You will be charged £1:50 per text</strong> plus network operators fee for each text you send and that will be at a maximum amount of 160 characters per text-in order to keep it brief and cost effective-you will then receive a carefully considered proffessional response that we hope will give you some guidance and relief.</li>
      </ul>
    </div>
    <hr class="divider">
    <p class="small-print">**Important terms &amp; conditions you are asked to readthese clearly before making contact. You must get the bill payers permission before using this service we do not take responsibility for any action you may take in relation to our guidance and feedback. We will not tell you what you should or should not do, we will guide rather than direct. There will be a maximum of 5 texts per correspondance this is to ensure it is a cost effective solution for you. Texts are charged at £1:50** plus network providers standard rate.</p>
  </div>
</section>

</body>
</html>
```